KAV cards & more
Business cards, fax cover sheet, letterhead, envelopes, powerpoint slide template
Modern
Tad Willers
Owner
17 Lindgate Row Harlow Falls, NJ 07990
twkav@mailvane.net
Please integrate my already-completed company logo (attached) in a clean, modern design for business cards, Fax cover sheet, letterhead, envelopes, and powerpoint slide template

```html
<!DOCTYPE html>
<html lang="en">
<head>
<meta charset="utf-8">
<title>KAV Stationery Set</title>
<link href="https://fonts.googleapis.com/css2?family=Montserrat:wght@400;600;700;800&display=swap" rel="stylesheet">
<style>
  :root{
    --canvas:#d9d9d9;
    --green-dark:#1f7a22;
    --green:#2f9a2c;
    --green-light:#7cc242;
    --silver-1:#ffffff;
    --silver-2:#d2d4d2;
    --ink:#333333;
    --muted:#6f6f6f;
    --panel:#e9ebe9;
  }
  html,body{margin:0;padding:0;overflow:hidden;}
  body{width:1200px;height:901px;background:var(--canvas);position:relative;font-family:"Montserrat",Arial,sans-serif;}
  .piece{position:absolute;display:block;box-shadow:0 4px 10px rgba(0,0,0,.25);}
  .business-card{left:61px;top:44px;width:669px;height:382px;}
  .fax-sheet{left:774px;top:224px;width:389px;height:238px;}
  .letterhead{left:97px;top:477px;width:463px;height:107px;}
  .envelope{left:61px;top:596px;width:523px;height:256px;}
  .slide{left:621px;top:462px;width:528px;height:378px;}
  text{font-family:"Montserrat",Arial,sans-serif;}
  .brand{font-weight:800;fill:var(--green);}
  .tagline{fill:var(--muted);}
</style>
</head>
<body>
<svg width="0" height="0" style="position:absolute">
  <defs>
    <linearGradient id="green-band" x1="0" y1="0" x2="1" y2="1">
      <stop offset="0" stop-color="var(--green-light)"/>
      <stop offset="1" stop-color="var(--green-dark)"/>
    </linearGradient>
    <linearGradient id="silver" x1="0" y1="0" x2="0" y2="1">
      <stop offset="0" stop-color="var(--silver-1)"/>
      <stop offset="1" stop-color="var(--silver-2)"/>
    </linearGradient>
    <linearGradient id="photo-tones" x1="0" y1="0" x2="0" y2="1">
      <stop offset="0" stop-color="#a9c3d6"/>
      <stop offset="0.6" stop-color="#5f7f8f"/>
      <stop offset="1" stop-color="#4c5a4a"/>
    </linearGradient>
  </defs>
</svg>

<!-- Business card -->
<svg class="piece business-card" viewBox="0 0 669 382">
  <rect width="669" height="382" fill="url(#green-band)"/>
  <path d="M0 0 H560 C520 150 380 300 0 330 Z" fill="url(#silver)"/>
  <circle cx="82" cy="112" r="36" fill="var(--green)"/>
  <text class="brand" x="135" y="134" font-size="60">KAV</text>
  <text class="tagline" x="137" y="162" font-size="13">Kestrel Avenue Ventures, LLC</text>
  <g fill="#fff" text-anchor="end">
    <text x="645" y="236" font-size="28" font-weight="700">Tad Willers</text>
    <text x="645" y="268" font-size="20">Owner</text>
    <g font-size="15">
      <text x="645" y="300">17 Lindgate Row</text>
      <text x="645" y="318">Harlow Falls, NJ 07990</text>
      <text x="645" y="336">Cell: 908.555.0142</text>
      <text x="645" y="354">Fax: 908.555.0187</text>
      <text x="645" y="372">Email: twkav@mailvane.net</text>
    </g>
  </g>
</svg>

<!-- Fax cover sheet -->
<svg class="piece fax-sheet" viewBox="0 0 389 238">
  <rect width="389" height="238" fill="#fff"/>
  <path d="M0 0 H389 V44 H250 C190 44 150 56 110 56 H0 Z" fill="url(#green-band)"/>
  <path d="M0 0 H220 C200 28 160 40 110 44 C70 47 30 50 0 52 Z" fill="url(#silver)"/>
  <circle cx="22" cy="24" r="10" fill="var(--green)"/>
  <text class="brand" x="38" y="31" font-size="20">KAV</text>
  <g fill="#fff" font-size="6">
    <text x="240" y="14">17 Lindgate Row</text>
    <text x="240" y="22">Harlow Falls, NJ 07990</text>
    <text x="315" y="14">Cell: 908.555.0142</text>
    <text x="315" y="22">Fax: 908.555.0187</text>
  </g>
  <text x="14" y="95" font-size="26" font-weight="600" fill="var(--ink)">FAX</text>
  <g font-size="9" fill="var(--ink)" stroke-width="0.8">
    <text x="14" y="117">To:</text><line x1="58" y1="118" x2="170" y2="118" stroke="var(--ink)"/>
    <text x="14" y="130">From:</text><line x1="58" y1="131" x2="170" y2="131" stroke="var(--ink)"/>
    <text x="14" y="143">Address:</text><line x1="58" y1="144" x2="170" y2="144" stroke="var(--ink)"/>
    <text x="14" y="156">Zip:</text><line x1="58" y1="157" x2="170" y2="157" stroke="var(--ink)"/>
    <text x="14" y="169">State:</text><line x1="58" y1="170" x2="170" y2="170" stroke="var(--ink)"/>
    <text x="205" y="117">Date:</text><line x1="245" y1="118" x2="370" y2="118" stroke="var(--ink)"/>
    <text x="205" y="130">Subject:</text><line x1="245" y1="131" x2="370" y2="131" stroke="var(--ink)"/>
    <text x="205" y="143">Pages:</text><line x1="245" y1="144" x2="370" y2="144" stroke="var(--ink)"/>
    <rect x="205" y="161" width="7" height="7" fill="none" stroke="var(--ink)"/><text x="216" y="168">Urgent</text>
    <rect x="258" y="161" width="7" height="7" fill="none" stroke="var(--ink)"/><text x="269" y="168">For Review</text>
    <rect x="328" y="161" width="7" height="7" fill="none" stroke="var(--ink)"/><text x="339" y="168">Reply</text>
  </g>
</svg>

<!-- Letterhead -->
<svg class="piece letterhead" viewBox="0 0 463 107">
  <rect width="463" height="107" fill="#fff"/>
  <path d="M0 0 H463 V48 H320 C240 48 200 66 150 66 H0 Z" fill="url(#green-band)"/>
  <path d="M0 0 H260 C230 38 170 54 110 58 C70 60 30 61 0 62 Z" fill="url(#silver)"/>
  <circle cx="28" cy="30" r="13" fill="var(--green)"/>
  <text class="brand" x="48" y="40" font-size="28">KAV</text>
  <g fill="#fff" font-size="7">
    <text x="275" y="14">17 Lindgate Row</text>
    <text x="275" y="24">Harlow Falls, NJ 07990</text>
    <text x="372" y="14">Cell: 908.555.0142</text>
    <text x="372" y="24">Fax: 908.555.0187</text>
    <text x="372" y="34">twkav@mailvane.net</text>
  </g>
</svg>

<!-- Envelope -->
<svg class="piece envelope" viewBox="0 0 523 256">
  <rect width="523" height="256" fill="#fff"/>
  <path d="M0 0 H200 C170 40 90 70 0 75 Z" fill="url(#silver)"/>
  <circle cx="30" cy="38" r="14" fill="var(--green)"/>
  <text class="brand" x="52" y="48" font-size="30">KAV</text>
  <text class="tagline" x="54" y="62" font-size="7">Kestrel Avenue Ventures, LLC</text>
  <rect x="30" y="168" width="190" height="55" fill="#fff" stroke="#b5b5b5" stroke-width="1.5"/>
  <path d="M523 256 H320 C330 200 380 160 523 150 Z" fill="url(#green-band)"/>
  <g fill="#fff" font-size="8" text-anchor="end">
    <text x="510" y="180">17 Lindgate Row</text>
    <text x="510" y="192">Harlow Falls, NJ 07990</text>
    <text x="510" y="204">Cell: 908.555.0142</text>
    <text x="510" y="216">Fax: 908.555.0187</text>
    <text x="510" y="228">Email: twkav@mailvane.net</text>
  </g>
</svg>

<!-- Slide template -->
<svg class="piece slide" viewBox="0 0 528 378">
  <rect width="528" height="378" fill="url(#green-band)"/>
  <path d="M0 0 H250 C220 40 150 70 0 80 Z" fill="url(#silver)"/>
  <circle cx="28" cy="34" r="14" fill="var(--green)"/>
  <text class="brand" x="50" y="45" font-size="30">KAV</text>
  <text x="500" y="52" font-size="24" font-weight="700" fill="#fff" text-anchor="end">Slide Title</text>
  <rect x="25" y="80" width="480" height="278" rx="10" fill="var(--panel)"/>
  <rect x="45" y="100" width="200" height="238" fill="url(#photo-tones)" role="img" aria-label="Photograph of modern glass office towers"/>
  <g font-size="11" fill="var(--ink)">
    <text x="265" y="130">• Lorem ipsum dolor sit amet,</text>
    <text x="265" y="144">consectetur adipiscing elit.</text>
    <text x="265" y="160">• Quisque enim nisl, posuere ut</text>
    <text x="265" y="174">sagittis sed, vestibulum et arcu.</text>
    <text x="265" y="190">• Suspendisse pretium nisl tristique</text>
    <text x="265" y="204">sapien pulvinar non imperdiet justo</text>
    <text x="265" y="218">scelerisque.</text>
    <text x="265" y="234">• Nunc blandit facilisis quam et</text>
    <text x="265" y="248">dictum. Quisque cursus tempus</text>
    <text x="265" y="262">quis massa.</text>
  </g>
</svg>
</body>
</html>
```